£500 POUND FOR A4 8 page booklet

to take 4 of my already done leaflet and make one a4 8 page booklet. The colour themes are green for pelmar dom bespoke timber frame and red for the rest. The front page needs to be the kestamore resin followed by another two pages of it www.kestamoreresin.co.uk. then two pages of pelmar dom then two pages of nolvo ridge then 1 page of spray protection (making sure you mention tower blocks in london )www.nolvo-ridge.co.uk and www.pelmar-dom.co.uk
i need the booklet to look way more professional than what these flyers are (grown up ) i can give more information bram@tenbyholdings.com
construction

```html
<!DOCTYPE html>
<html lang="en">
<head>
<meta charset="utf-8">
<title>Nolvo Ridge – Booklet Cover Spread</title>
<link rel="stylesheet" href="https://fonts.googleapis.com/css2?family=Cinzel:wght@400;600&family=Arimo:wght@400;600&display=swap">
<style>
  :root{
    --backdrop:#e9e6e2;
    --page:#ffffff;
    --page-shade:#dedfe2;
    --crimson:#8e1b1f;
    --magenta:#e2358f;
    --ink:#2b2b2b;
    --muted:#555;
    --wall-top:#8a9699;
    --wall-mid:#b4c3c8;
    --wall-low:#a7b8be;
  }
  *{margin:0;padding:0;box-sizing:border-box}
  html,body{width:1200px;height:907px;overflow:hidden;background:var(--backdrop)}
  body{position:relative;font-family:"Arimo",Arial,sans-serif;color:var(--ink)}
  .spread{position:absolute;left:34px;top:53px;width:1132px;height:800px;box-shadow:0 10px 30px rgba(0,0,0,.25)}
  .page{position:absolute;top:0;width:566px;height:800px;overflow:hidden}
  .page--back{left:0;background:linear-gradient(155deg,#eceded 0%,#fff 22%,#fff 48%,#f3f3f4 75%,var(--page-shade) 100%)}
  .page--front{left:566px;background:linear-gradient(200deg,#f0f0f1 0%,#fff 18%,#fff 55%,var(--page-shade) 100%)}
  .spine{position:absolute;left:560px;top:0;width:12px;height:800px;
         background:linear-gradient(90deg,rgba(0,0,0,0) 0%,rgba(0,0,0,.10) 50%,rgba(0,0,0,0) 100%);z-index:3}

  .rule{position:absolute;left:0;right:0;height:3px;z-index:2}
  .rule--crimson{background:var(--crimson)}
  .rule--magenta{background:var(--magenta)}
  .photo-band{position:absolute;left:0;right:0;top:163px;height:300px;z-index:1;
        background:linear-gradient(180deg,var(--wall-top) 0%,#9aa7aa 30%,var(--wall-mid) 46%,var(--wall-low) 100%)}

  /* back cover */
  .contact__title{position:absolute;left:60px;top:500px;font-family:"Cinzel",serif;font-weight:600;font-size:20px;color:var(--crimson)}
  .contact__line{position:absolute;display:flex;gap:6px;font-size:12px;line-height:17px;color:var(--ink)}
  .contact__line svg{flex:none;margin-top:3px}
  .brand{display:flex;align-items:center;gap:8px}
  .brand__dot{width:12px;height:12px;border-radius:50%;background:var(--crimson)}
  .brand__name{font-family:"Cinzel",serif;font-weight:600;color:var(--crimson);white-space:nowrap}
  .brand__divider{width:1px;align-self:stretch;background:var(--crimson)}
  .back-brand{position:absolute;left:60px;top:640px}
  .back-brand .brand__name{font-size:14px}
  .visit{position:absolute;left:210px;top:628px}
  .visit__label{font-family:"Cinzel",serif;font-size:14px;color:var(--muted)}
  .visit__url{font-size:13px;color:var(--magenta)}
  .copyright{position:absolute;left:60px;top:735px;font-size:9px;line-height:12px;color:var(--muted)}
  .double-rule{position:absolute;height:7px;border-top:2px solid var(--magenta);border-bottom:2px solid var(--crimson)}

  /* front cover */
  .front-brand{position:absolute;left:0;right:0;top:52px;display:flex;justify-content:center}
  .front-brand .brand__name{font-size:22px}
  .front-brand__tag{position:absolute;left:0;right:0;top:90px;text-align:center;font-size:8px;letter-spacing:.5px;text-transform:uppercase;color:var(--muted)}
  .feature{position:absolute;top:398px;width:136px;height:136px;border-radius:50%;border:5px solid var(--crimson);z-index:4;
           box-shadow:0 0 0 4px #fff,0 5px 12px rgba(0,0,0,.3)}
  .feature--one{left:56px;background:linear-gradient(160deg,#6f8fa3,#2f3e4c)}
  .feature--two{left:208px;background:linear-gradient(160deg,#b9c7d6,#3d55a0)}
  .feature--three{left:360px;background:linear-gradient(160deg,#b79ad6,#e8e4ef)}
  .headline{position:absolute;left:0;right:0;top:588px;text-align:center;font-family:"Cinzel",serif;color:var(--crimson);line-height:1.1}
  .headline__lead{display:block;font-size:30px;font-weight:600}
  .headline__sub{display:block;font-size:18px;margin-top:4px}
  .front-url{position:absolute;left:0;right:0;top:688px;text-align:center;font-size:18px;font-weight:600;color:var(--ink)}
</style>
</head>
<body>
<div class="spread">

  <section class="page page--back">
    <h2 class="contact__title">Get in Touch</h2>
    <p class="contact__line" style="left:60px;top:534px;width:220px">
      <svg width="10" height="10" viewBox="0 0 10 10"><path d="M5 0 L10 5 H8.5 V10 H1.5 V5 H0 Z" fill="var(--magenta)"/></svg>
      <span>Unit 9a, The Old Larchmere Buildings, Kiln Lane, Ashcombe, Bedfordshire, ZZ9 4QT, United Kingdom</span>
    </p>
    <p class="contact__line" style="left:300px;top:512px">
      <svg width="10" height="11" viewBox="0 0 10 11"><path d="M2 0 L4 3 L3 4.5 Q4.5 7 6.5 8 L8 7 L10 9 L8.5 11 Q2 9 0 1.5 Z" fill="var(--magenta)"/></svg>
      <span>01632 960418 or 07700 900 262.</span>
    </p>
    <p class="contact__line" style="left:300px;top:536px">
      <svg width="11" height="9" viewBox="0 0 11 9"><rect width="11" height="8" y=".5" fill="var(--magenta)"/><path d="M0 .5 L5.5 5 L11 .5" stroke="#fff" fill="none"/></svg>
      <span>info@nolvo-ridge.co.uk</span>
    </p>

    <div class="back-brand brand">
      <span class="brand__dot"></span>
      <span class="brand__name">Nolvo Ridge</span>
    </div>
    <div class="visit">
      <p class="visit__label">For more information Visit Us</p>
      <p class="visit__url">www.kestamoreresin.co.uk</p>
    </div>
    <div class="double-rule" style="left:210px;right:0;top:700px"></div>
    <p class="copyright">Copyright 2016 - Nolvo Ridge.<br>All rights reserved.</p>
  </section>

  <section class="page page--front">
    <div class="front-brand brand">
      <span class="brand__dot"></span>
      <span class="brand__name">Nolvo Ridge</span>
      <span class="brand__divider"></span>
      <span class="brand__name">Kestamore Resin</span>
    </div>
    <p class="front-brand__tag">Liquid applied airtight membranes</p>

    <div class="feature feature--one" role="img" aria-label="Photo of a worker spraying an interior wall"></div>
    <div class="feature feature--two" role="img" aria-label="Photo of a worker applying blue membrane to blockwork"></div>
    <div class="feature feature--three" role="img" aria-label="Photo of a worker in protective suit insulating a roof space"></div>

    <h1 class="headline">
      <span class="headline__lead">Specialist in</span>
      <span class="headline__sub">Roof Renovation and Insulation Company</span>
    </h1>
    <div class="double-rule" style="left:60px;right:60px;top:670px"></div>
    <p class="front-url">www.kestamoreresin.co.uk</p>
  </section>

  <div class="rule rule--crimson" style="top:150px"></div>
  <div class="rule rule--magenta" style="top:157px"></div>
  <div class="photo-band" role="img" aria-label="Wide photo across both covers of a worker in hi-vis spraying liquid membrane onto a grey-blue building wall below a row of windows"></div>
  <div class="rule rule--magenta" style="top:465px"></div>
  <div class="rule rule--crimson" style="top:472px"></div>
  <div class="spine"></div>

</div>
</body>
</html>
```